Classy, Elegant, Simple Business Card Design

Looking to have a classy, simple, and elegant design. Want a top notch designed business card. I really like the look of the new brivo credit card. I also like the design I attached. I am trying to reach 21-29 year old females for booking us for there wedding or event. We offer Disc Jockey Service, Photo Booth Rentals, and Uplighting .

Target Market(s)

21-28 year old females

Contact Information for Business Card

Has to have logo, website, email, and phone number

Font styles to use
Other font styles liked:
• open to font choice, modern, clean
Designer to choose
33a6d7
0791cd
0555a3
ffffff

Requirements
Must have
• Has to have logo, website, email, and phone number
Nice to have
• I really like the design of the new brivo credit card. I also included my logo and some designs I like
Should not have
• clutter or too much info

```html
<!DOCTYPE html>
<html lang="en">
<head>
<meta charset="utf-8">
<title>Tidewell Event Group – Business Card</title>
<link rel="stylesheet" href="https://fonts.googleapis.com/css2?family=Lato:wght@400;700&display=swap">
<style>
  :root {
    --backdrop: #2b2b2d;
    --card: #1c1d20;
    --card-edge: #26272a;
    --blue-light: #33a6d7;
    --blue: #0791cd;
    --blue-deep: #0555a3;
    --white: #ffffff;
    --text-soft: #e6e8ea;
    --rule: #6b6e73;
  }
  * { box-sizing: border-box; margin: 0; padding: 0; }
  html, body {
    width: 1200px; height: 1108px; overflow: hidden;
    background: var(--backdrop);
    font-family: "Lato", sans-serif;
  }
  .sheet {
    position: relative; width: 1200px; height: 1108px;
    display: flex; justify-content: center; align-items: center; gap: 60px;
  }
  .card {
    width: 420px; height: 700px;
    background: var(--card);
    border: 1px solid var(--card-edge);
    border-radius: 24px;
    position: relative;
    overflow: hidden;
  }
  /* Front */
  .card--front {
    display: flex; flex-direction: column; align-items: center;
    padding-top: 150px;
  }
  .brand-mark {
    display: flex; align-items: center; gap: 14px;
  }
  .brand-mark__dot {
    width: 18px; height: 18px; border-radius: 50%;
    background: var(--blue);
  }
  .brand-name {
    color: var(--blue);
    font-weight: 700;
    font-size: 34px;
    letter-spacing: 1px;
    line-height: 1.15;
    text-align: center;
  }
  .contact {
    margin-top: 150px;
    width: 300px;
    display: flex; flex-direction: column; align-items: center;
  }
  .contact__icons {
    width: 100%;
    display: flex; align-items: center; gap: 8px;
  }
  .contact__rule {
    flex: 1; height: 1px; background: var(--rule);
  }
  .icon {
    width: 26px; height: 26px; border-radius: 50%;
    background: var(--blue);
    display: flex; align-items: center; justify-content: center;
  }
  .icon svg { width: 14px; height: 14px; }
  .contact__lines {
    margin-top: 16px;
    text-align: center;
    color: var(--text-soft);
    font-size: 19px;
    line-height: 1.35;
  }
  .divider {
    width: 240px; height: 1px; background: var(--rule);
    margin: 14px 0;
  }
  .services {
    text-align: center;
    color: var(--white);
    font-size: 20px;
    line-height: 1.3;
  }
  /* Back */
  .back__pattern {
    position: absolute; inset: 0;
    background: linear-gradient(160deg, #212225 0%, #1c1d20 55%, #1f2023 100%);
  }
  .back__name {
    position: absolute; left: 0; right: 0; top: 440px;
    text-align: center;
    color: var(--blue);
    font-weight: 700;
    font-size: 26px;
    letter-spacing: 1px;
  }
</style>
</head>
<body>
  <main class="sheet">
    <section class="card card--front" aria-label="Card front">
      <div class="brand-mark">
        <span class="brand-mark__dot"></span>
        <h1 class="brand-name">Tidewell<br>Event Group</h1>
      </div>

      <div class="contact">
        <div class="contact__icons">
          <span class="contact__rule"></span>
          <span class="icon" aria-label="Phone">
            <svg viewBox="0 0 24 24"><path fill="#fff" d="M6.6 10.8a15.1 15.1 0 0 0 6.6 6.6l2.2-2.2c.3-.3.7-.4 1-.2 1.1.4 2.3.6 3.6.6.6 0 1 .4 1 1V20c0 .6-.4 1-1 1C10.6 21 3 13.4 3 4c0-.6.4-1 1-1h3.5c.6 0 1 .4 1 1 0 1.3.2 2.5.6 3.6.1.3 0 .7-.2 1z"/></svg>
          </span>
          <span class="icon" aria-label="Email">
            <svg viewBox="0 0 24 24"><path fill="#fff" d="M3 5h18v14H3z"/><path fill="none" stroke="#0791cd" stroke-width="2" d="M3 6l9 7 9-7"/></svg>
          </span>
          <span class="icon" aria-label="Website">
            <svg viewBox="0 0 24 24"><circle cx="12" cy="12" r="9" fill="none" stroke="#fff" stroke-width="2"/><path fill="none" stroke="#fff" stroke-width="1.6" d="M3 12h18M12 3c3 3 3 15 0 18M12 3c-3 3-3 15 0 18"/></svg>
          </span>
          <span class="contact__rule"></span>
        </div>
        <p class="contact__lines">
          044-987 654 321<br>
          hello@tidewell.com<br>
          www.tidewellevents.com
        </p>
        <span class="divider"></span>
        <p class="services">
          Disc Jockey Service | Uplighting<br>
          Photo Booth Rentals
        </p>
      </div>
    </section>

    <section class="card card--back" aria-label="Card back">
      <div class="back__pattern" role="img" aria-label="Faint repeating brand pattern across the card back"></div>
      <p class="back__name">Tidewell</p>
    </section>
  </main>
</body>
</html>
```